Bag packaging design of sliced bread

The project is for design of line of sliced bread with different flavours. The brand of the bread will be "Valorina". The shape of the bread will be oval. The bread will be packed in a bag. I attach the layout of the bag. The bag will be closed with a plastic clip. I attach images of similar products. The idea is to have one main design and then each colour to be different type of bread like those in the images 2 and 5.

```html
<!DOCTYPE html>
<html lang="en">
<head>
<meta charset="utf-8">
<title>Valorina sliced bread bag line</title>
<link rel="stylesheet" href="https://fonts.googleapis.com/css2?family=Nunito:wght@900&family=PT+Sans:wght@400&family=Jost:wght@600&display=swap">
<style>
:root{
  --backdrop:#858585;
  --ink:#ffffff;
  --green-light:#86c53a;--green-dark:#4f9a1c;
  --blue-light:#5aa9bd;--blue-dark:#3a7f93;
  --pink-light:#c8527f;--pink-dark:#8e2550;
  --orange-light:#d8861c;--orange-dark:#a9590a;
}
*{margin:0;padding:0;box-sizing:border-box}
html,body{width:1200px;height:735px;overflow:hidden;background:var(--backdrop)}
.sheet{position:absolute;left:16px;top:52px;width:1172px;height:655px;display:grid;grid-template-columns:repeat(4,1fr)}
.bag{position:relative;display:grid;grid-template-rows:152px 164px 1fr;color:var(--ink)}
.wood,.front{width:100%;height:100%;background:var(--wood)}
.bag--rye{--wood:linear-gradient(90deg,var(--green-light),var(--green-dark) 60%,var(--green-light))}
.bag--multigrain{--wood:linear-gradient(90deg,var(--blue-dark),var(--blue-light) 50%,var(--blue-dark))}
.bag--wheat{--wood:linear-gradient(90deg,var(--pink-light),var(--pink-dark) 70%,var(--pink-light))}
.bag--white{--wood:linear-gradient(90deg,var(--orange-dark),var(--orange-light) 50%,var(--orange-dark))}
.window{position:relative}
.window .loaf{position:absolute;inset:0}
.bag--rye .loaf{background:linear-gradient(90deg,#c97a55,#dca37f 60%,#e3bb98)}
.bag--multigrain .loaf{background:linear-gradient(90deg,#d9863a,#e89a4c 50%,#eedbb0 70%,#f0e2c0)}
.bag--wheat .loaf{background:linear-gradient(180deg,#b78a44,#9e7430 50%,#b88c45)}
.bag--white .loaf{background:linear-gradient(180deg,#e7a15c,#d97b2e 50%,#e59a52)}
.window svg{position:absolute;inset:0;width:100%;height:100%}
.window-label{position:absolute;left:0;right:0;top:78px;text-align:center;font:600 15px/1 'Jost',sans-serif;letter-spacing:2px}
.front{position:relative;text-align:center}
.brand{position:absolute;left:0;right:0;top:58px;font:900 30px/1 'Nunito',sans-serif;display:flex;align-items:center;justify-content:center;gap:8px}
.brand::before{content:"";width:12px;height:12px;border-radius:50%;background:#000}
.variety{position:absolute;left:0;right:0;top:142px;font:900 38px/0.95 'Nunito',sans-serif}
.variety .big{font-size:46px;display:block}
.claims{position:absolute;left:0;right:0;top:226px;font:400 8.6px/9px 'PT Sans',sans-serif}
.net{position:absolute;left:0;right:0;top:290px;font:400 9px/1 'PT Sans',sans-serif}
</style>
</head>
<body>
<main class="sheet">
  <section class="bag bag--rye">
    <div class="wood" role="img" aria-label="Green painted wooden planks"></div>
    <div class="window">
      <div class="loaf" role="img" aria-label="Rye bread loaf seen through clear window"></div>
      <svg viewBox="0 0 293 164" preserveAspectRatio="none"><g stroke="#fff" stroke-width="3"><line x1="0" y1="0" x2="120" y2="67"/><line x1="180" y1="67" x2="293" y2="0"/><line x1="115" y1="108" x2="3" y2="164"/><line x1="180" y1="108" x2="290" y2="164"/></g></svg>
      <p class="window-label">WINDOW</p>
    </div>
    <div class="front">
      <p class="brand">Valorina</p>
      <h2 class="variety">rye<br>bread</h2>
      <p class="claims">FOLATE-ENRICHED<br>WITH VITAMINS AND MINERALS<br>ZERO TRANS FAT</p>
      <p class="net">Net Wt.&nbsp; 600g</p>
    </div>
  </section>
  <section class="bag bag--multigrain">
    <div class="wood" role="img" aria-label="Blue painted wooden planks"></div>
    <div class="window">
      <div class="loaf" role="img" aria-label="Multigrain bread loaf seen through clear window"></div>
      <svg viewBox="0 0 293 164" preserveAspectRatio="none"><g stroke="#fff" stroke-width="3"><line x1="0" y1="0" x2="120" y2="67"/><line x1="180" y1="67" x2="293" y2="0"/><line x1="115" y1="108" x2="3" y2="164"/><line x1="180" y1="108" x2="290" y2="164"/></g></svg>
      <p class="window-label">WINDOW</p>
    </div>
    <div class="front">
      <p class="brand">Valorina</p>
      <h2 class="variety">multi<span class="big">grain</span></h2>
      <p class="claims">FOLATE-ENRICHED<br>WITH VITAMINS AND MINERALS<br>ZERO TRANS FAT</p>
      <p class="net">Net Wt.&nbsp; 600g</p>
    </div>
  </section>
  <section class="bag bag--wheat">
    <div class="wood" role="img" aria-label="Magenta painted wooden planks"></div>
    <div class="window">
      <div class="loaf" role="img" aria-label="Sliced whole wheat bread seen through clear window"></div>
      <svg viewBox="0 0 293 164" preserveAspectRatio="none"><g stroke="#fff" stroke-width="3"><line x1="0" y1="0" x2="120" y2="67"/><line x1="180" y1="67" x2="293" y2="0"/><line x1="115" y1="108" x2="3" y2="164"/><line x1="180" y1="108" x2="290" y2="164"/></g></svg>
      <p class="window-label">WINDOW</p>
    </div>
    <div class="front">
      <p class="brand">Valorina</p>
      <h2 class="variety">whole<span class="big">wheat</span></h2>
      <p class="claims">FOLATE-ENRICHED<br>WITH VITAMINS AND MINERALS<br>ZERO TRANS FAT</p>
      <p class="net">Net Wt.&nbsp; 600g</p>
    </div>
  </section>
  <section class="bag bag--white">
    <div class="wood" role="img" aria-label="Amber stained wooden planks"></div>
    <div class="window">
      <div class="loaf" role="img" aria-label="Sliced soft white bread seen through clear window"></div>
      <svg viewBox="0 0 293 164" preserveAspectRatio="none"><g stroke="#fff" stroke-width="3"><line x1="0" y1="0" x2="120" y2="67"/><line x1="180" y1="67" x2="293" y2="0"/><line x1="115" y1="108" x2="3" y2="164"/><line x1="180" y1="108" x2="290" y2="164"/></g></svg>
      <p class="window-label">WINDOW</p>
    </div>
    <div class="front">
      <p class="brand">Valorina</p>
      <h2 class="variety">soft<span class="big">white</span></h2>
      <p class="claims">FOLATE-ENRICHED<br>WITH VITAMINS AND MINERALS<br>ZERO TRANS FAT</p>
      <p class="net">Net Wt.&nbsp; 600g</p>
    </div>
  </section>
</main>
</body>
</html>
```